vortane realty business card

We need a Business card for our new business. The logo was designed by ArtQuillo, and the text We want on the back is:
REAL ESTATE INVESTMENTS
- BUY, RENOVATE, SELL AND RENT RESIDENTIAL PROPERTIES
- FULL HOME REHABBING , REMODELING AND INTERIOR DESIGN
- HOME STAGING SERVICES
- WHOLESALE INVESTOR PROPERTIES
- MAKE CASH OFFERS ON HOUSES IN ANY CONDITION AND IN ANY SITUATION
- PRIVATE MONEY INVESTOR PROGRAMS WITH 6-12% RETURNS
- PAY CASH REWARDS FOR REFFERALS
- CONCIERGE SERVICE

```html
<!DOCTYPE html>
<html lang="en">
<head>
<meta charset="utf-8">
<title>Vortane Realty – Business Card</title>
<link rel="stylesheet" href="https://fonts.googleapis.com/css2?family=Open+Sans:wght@400;600&display=swap">
<style>
  :root {
    --stage: #3a3a3a;
    --card-white: #ffffff;
    --band-grey: #a6a7ab;
    --accent: #5fc3cf;
    --teal: #72c8cf;
    --text-grey: #808387;
    --text-dark: #222222;
    --white: #ffffff;
    --bullet: rgba(120,120,120,0.45);
  }
  * { margin: 0; padding: 0; box-sizing: border-box; }
  html, body { width: 1200px; height: 820px; overflow: hidden; }
  body {
    position: relative;
    background: var(--stage);
    font-family: "Open Sans", Arial, sans-serif;
  }
  .card {
    position: absolute;
    top: 258px;
    width: 471px;
    height: 270px;
    overflow: hidden;
  }
  /* Front */
  .card-front { left: 117px; background: var(--card-white); }
  .side-band {
    position: absolute; left: 0; top: 0; width: 31px; height: 100%;
    background: var(--band-grey);
  }
  .side-line {
    position: absolute; left: 32px; top: 0; width: 2px; height: 100%;
    background: var(--accent);
  }
  .brand { position: absolute; left: 57px; top: 36px; }
  .brand-mark {
    position: absolute; left: 0; top: 8px; width: 22px; height: 22px;
    background: var(--accent);
  }
  .brand-name {
    position: absolute; left: 66px; top: 0;
    font-size: 26px; font-weight: 400; color: var(--accent);
    white-space: nowrap; line-height: 36px;
  }
  .brand-tagline {
    position: absolute; left: 66px; top: 36px;
    font-size: 14px; letter-spacing: 1.2px; color: var(--text-grey);
    white-space: nowrap;
  }
  .person { position: absolute; left: 57px; top: 120px; }
  .person-name { font-size: 18px; color: var(--text-grey); line-height: 24px; }
  .person-role { font-size: 13px; color: var(--text-dark); line-height: 18px; }
  .contacts { position: absolute; left: 57px; top: 178px; list-style: none; }
  .contacts li {
    display: flex; align-items: center; height: 20px;
    font-size: 12.5px; color: var(--text-dark); white-space: nowrap;
  }
  .contacts svg { width: 12px; height: 12px; margin-right: 8px; flex: none; fill: var(--accent); }
  /* Back */
  .card-back { left: 628px; background: var(--teal); color: var(--white); }
  .services-title {
    position: absolute; left: 32px; top: 50px;
    font-size: 18px; font-weight: 400; letter-spacing: 0.2px;
    white-space: nowrap;
  }
  .services { position: absolute; left: 32px; top: 96px; right: 8px; list-style: none; }
  .services li {
    display: flex; align-items: center; height: 16px;
    font-size: 11.1px; white-space: nowrap;
  }
  .services li::before {
    content: ""; flex: none; width: 8px; height: 8px; margin-right: 6px;
    background: var(--bullet);
  }
</style>
</head>
<body>
  <section class="card card-front">
    <div class="side-band"></div>
    <div class="side-line"></div>
    <div class="brand">
      <span class="brand-mark"></span>
      <span class="brand-name">VORTANE Realty</span>
      <span class="brand-tagline">REAL ESTATE SOLUTIONS</span>
    </div>
    <div class="person">
      <p class="person-name">Milo Hartwell</p>
      <p class="person-role">Graphic Designer</p>
    </div>
    <ul class="contacts">
      <li><svg viewBox="0 0 12 12"><path d="M3 1l2 2.5-1.2 1.4a6 6 0 0 0 3.3 3.3L8.5 7 11 9l-1 2C5 11 1 7 1 2z"/></svg>0203 555 0142</li>
      <li><svg viewBox="0 0 12 12"><rect x="1" y="4" width="3" height="7"/><rect x="5" y="1" width="3" height="10"/><rect x="9" y="5" width="2" height="6"/></svg>0203 555 0178</li>
      <li><svg viewBox="0 0 12 12"><path d="M1 3h10v6H1z M1 3l5 3.5L11 3" fill="none" stroke="#5fc3cf" stroke-width="1.2"/></svg>Yourname@vortanerealty.com</li>
      <li><svg viewBox="0 0 12 12"><circle cx="6" cy="6" r="4.8" fill="none" stroke="#5fc3cf" stroke-width="1.2"/><path d="M1.5 6h9M6 1.2c-2 2.5-2 7 0 9.6M6 1.2c2 2.5 2 7 0 9.6" fill="none" stroke="#5fc3cf" stroke-width="0.9"/></svg>www.vortanerealty.com</li>
    </ul>
  </section>

  <section class="card card-back">
    <h2 class="services-title">REAL ESTATE INVESTMENTS</h2>
    <ul class="services">
      <li>BUY, RENOVATE, SELL AND RENT RESIDENTIAL PROPERTIES</li>
      <li>FULL HOME REHABBING , REMODELING AND INTERIOR DESIGN</li>
      <li>HOME STAGING SERVICES</li>
      <li>WHOLESALE INVESTOR PROPERTIES</li>
      <li>MAKE CASH OFFERS ON HOUSES IN ANY CONDITION AND IN ANY SITUATION</li>
      <li>PRIVATE MONEY INVESTOR PROGRAMS WITH 6-12% RETURNS</li>
      <li>PAY CASH REWARDS FOR REFFERALS</li>
      <li>CONCIERGE SERVICE</li>
    </ul>
  </section>
</body>
</html>
```